Brevane Advisory business card

Premium business card required
I have attached the brand as a powerpoint template but this can be made to look very up market, I have also attached my BIO for title reasons and to give you a feel for my skills
front of card
Darrel Voskuij
Managing Director Brevane Advisory
Retail, Customer-Led Experience, Transformation and Maximising Shareholder Return
Mobile +61(0)487395028
Email darrelbrevaneadvisory.example
back of card

BREVANE ADVISORY’ OFFERING

We transform customer environments to extract benefits while elevating service levels;
We release millions of dollars in self-funding through continuous improvement;
We see CX as a key differentiator, proactively guarding share from market disrupters;
We re-invent service and create front-end of the future.

```html
<!DOCTYPE html>
<html lang="en">
<head>
<meta charset="utf-8">
<title>Brevane Advisory – Business Card</title>
<link rel="stylesheet" href="https://fonts.googleapis.com/css2?family=Montserrat:wght@600;700&family=Source+Sans+3:wght@400;500&display=swap">
<style>
  :root {
    --stage: #202020;
    --card-white: #ffffff;
    --card-grey: #5b5b5b;
    --gold: #cdaf34;
    --ink: #4a4a4a;
    --ink-soft: #555555;
    --band-grey: #525252;
    --text-light: #f4f4f4;
  }
  * { margin: 0; padding: 0; box-sizing: border-box; }
  html, body {
    width: 1200px; height: 900px; overflow: hidden;
    background: var(--stage);
  }
  .stage { position: relative; width: 1200px; height: 900px; }

  .card { position: absolute; top: 306px; width: 440px; height: 272px; overflow: hidden; }
  .card--front { left: 149px; background: var(--card-white); }
  .card--back { left: 608px; width: 441px; background: var(--card-grey); }

  .holder-name {
    position: absolute; left: 25px; top: 27px;
    font: 600 17px/1 "Montserrat", sans-serif;
    color: var(--gold); letter-spacing: 0.2px;
  }
  .holder-title {
    position: absolute; left: 24px; top: 49px; width: 230px;
    font: 400 12.3px/16.5px "Source Sans 3", sans-serif;
    color: var(--ink-soft);
  }
  .brand {
    position: absolute; right: 25px; top: 162px;
    display: flex; align-items: center; gap: 9px;
  }
  .brand-dot { width: 14px; height: 14px; border-radius: 50%; background: var(--gold); }
  .brand-name {
    font: 700 20px/1 "Montserrat", sans-serif;
    color: var(--ink); letter-spacing: 0.2px;
  }
  .contact {
    position: absolute; left: 24px; top: 206px; list-style: none;
    font: 400 12.5px/16.5px "Source Sans 3", sans-serif;
    color: var(--ink);
  }
  .contact li { display: flex; align-items: center; gap: 5px; }
  .contact svg { width: 9px; height: 9px; fill: var(--gold); flex: none; }
  .footer-bands { position: absolute; left: 0; bottom: 0; width: 440px; height: 21px; }

  .offering-heading {
    position: absolute; left: 33px; top: 34px;
    font: 400 15px/1 "Source Sans 3", sans-serif;
    color: var(--gold); text-transform: uppercase; letter-spacing: 0.1px;
  }
  .offering-list {
    position: absolute; left: 33px; top: 72px; width: 340px; list-style: none;
    font: 500 12.3px/16px "Source Sans 3", sans-serif;
    color: var(--text-light);
  }
  .offering-list li { position: relative; padding-left: 13px; margin-bottom: 15.5px; }
  .offering-list li::before {
    content: ""; position: absolute; left: 1px; top: 5px;
    width: 6px; height: 6px; border-radius: 50%; background: var(--gold);
  }
</style>
</head>
<body>
<main class="stage">
  <section class="card card--front" aria-label="Card front">
    <h1 class="holder-name">DARREL VOSKUIJ</h1>
    <p class="holder-title">Managing Director Brevane Advisory Retail, Customer-Led Experience, Transformation and Maximising Shareholder Return</p>

    <div class="brand">
      <span class="brand-dot"></span>
      <span class="brand-name">BREVANE ADVISORY</span>
    </div>

    <ul class="contact">
      <li>
        <svg viewBox="0 0 10 10" aria-hidden="true"><path d="M2 0.5 3.6 2.6 2.7 3.6Q3.6 5.8 6.4 7.3L7.4 6.4 9.5 8 8.4 9.5Q1 8.2 0.5 1.6Z"/></svg>
        <span>+61(0)487395028</span>
      </li>
      <li>
        <svg viewBox="0 0 10 10" aria-hidden="true"><path d="M0 2h10v0.6L5 5.6 0 2.6Z M0 3.6 5 6.6 10 3.6V8.5H0Z"/></svg>
        <span>darrelbrevaneadvisory.example</span>
      </li>
    </ul>

    <svg class="footer-bands" viewBox="0 0 440 21" aria-hidden="true">
      <polygon points="0,7 197,7 188,21 0,21" fill="var(--gold)"/>
      <polygon points="201,1 440,1 440,21 188,21" fill="var(--band-grey)"/>
    </svg>
  </section>

  <section class="card card--back" aria-label="Card back">
    <h2 class="offering-heading">Brevane Advisory’ Offering</h2>
    <ul class="offering-list">
      <li>We transform customer environments to extract benefits while elevating service levels;</li>
      <li>We release millions of dollars in self-funding through continuous improvement;</li>
      <li>We see CX as a key differentiator, proactively guarding share from market disrupters;</li>
      <li>We re-invent service and create front-end of the future.</li>
    </ul>
  </section>
</main>
</body>
</html>
```